Design for Tolvo Ginger Chewy Candy!

Hello! We are Tolvo Enterprises Corp, a food manufacturer and distributor based in Los Angeles, CA. We manufacture Chips, Cookies, Juices, Dairy, and last but not least, Candies! We are launching our Ginger Chewy Candy soon and we need a great design for it!

Our Ginger Chewy Candy is a perfect mixture between sweet and spicy from the ginger itself. Tolvo Ginger Chewy Candy a good relief for sore throat and nausea.

Now, other than a great design, we also welcome brand suggestions for the candy.
If you can come up with a logo for the Ginger Candy, that would be swell!

We are open to unique and out of the box design. We chose a few color schemes for the design, but feel free to step out of the box if you feel it suits the brand.

We don't have the exact size for the plastic pouch, but it should be a generic small plastic pouch size (approximately 4 oz resealable plastic pouch)

Please have fun designing the project, we can't wait to see all the great designs!

Cheers!

Target Market(s)

USA and Asian market
Age 30-70
Male and Female

Industry/Entity Type

Manufacture

Font styles to use
Serif
Sans Serif
Decorative

Colors
fff3d1
fee18a
fece3e
fbc994
fce8d3

Requirements
Must have
• Tolvo Logo
• A picture of ginger (illustrations or photographs are welcome)
Nice to have
• Coating suggestions like Matte surface or SPOT UV
• Give us ideas of what the name of the chewy candy should be. Product name ideas are welcome!

```html
<!DOCTYPE html>
<html lang="en">
<head>
<meta charset="utf-8">
<title>Tolvo Ginger Chewy Candy – Pouch Front</title>
<link rel="stylesheet" href="https://fonts.googleapis.com/css2?family=Fredoka:wght@600&family=Oswald:wght@500&family=Chewy&display=swap">
<style>
  :root{
    --canvas:#f4f5f7;
    --crimp-yellow:#f2d21a;
    --crimp-line:#e0b800;
    --leaf-green:#8dc22a;
    --leaf-green-deep:#4f9a1c;
    --leaf-green-light:#c6e05a;
    --sun-yellow:#f5cf12;
    --navy:#1d2a7a;
    --sky-blue:#2aa3df;
    --brand-yellow:#f7d417;
    --pouch-white:#ffffff;
    --seal-grey:#e3e5ea;
    --ginger-tan:#c9a672;
    --ginger-gold:#f1c22a;
  }
  html,body{margin:0;padding:0;overflow:hidden;}
  body{width:1200px;height:960px;background:var(--canvas);display:flex;align-items:center;justify-content:center;}
  .pouch{width:600px;height:860px;display:block;filter:drop-shadow(0 10px 24px rgba(0,0,0,.12));}
  .brand-mark{font-family:"Fredoka",sans-serif;font-weight:600;fill:var(--navy);}
  .product-name{font-family:"Fredoka",sans-serif;font-weight:600;fill:var(--brand-yellow);}
  .flavour-banner-text{font-family:"Oswald",sans-serif;font-weight:500;fill:#fff;letter-spacing:1px;}
  .tagline{font-family:"Chewy",cursive;fill:var(--sun-yellow);}
  .tagline-shadow{font-family:"Chewy",cursive;fill:var(--navy);}
  .net-weight{font-family:"Oswald",sans-serif;font-weight:500;fill:var(--navy);}
</style>
</head>
<body>
<svg class="pouch" viewBox="0 0 600 860" xmlns="http://www.w3.org/2000/svg">
  <defs>
    <pattern id="crimp-top" width="600" height="8" patternUnits="userSpaceOnUse">
      <rect width="600" height="8" fill="var(--crimp-yellow)"/>
      <rect y="6" width="600" height="2" fill="var(--crimp-line)"/>
    </pattern>
    <pattern id="crimp-bottom" width="600" height="8" patternUnits="userSpaceOnUse">
      <rect width="600" height="8" fill="#f7f8fa"/>
      <rect y="6" width="600" height="2" fill="var(--seal-grey)"/>
    </pattern>
    <pattern id="pennant-lines" width="220" height="7" patternUnits="userSpaceOnUse">
      <rect width="220" height="7" fill="#fff"/>
      <rect y="5" width="220" height="2" fill="#eceff3"/>
    </pattern>
    <radialGradient id="field-green" cx="50%" cy="40%" r="65%">
      <stop offset="0" stop-color="var(--leaf-green-light)"/>
      <stop offset=".55" stop-color="var(--leaf-green)"/>
      <stop offset="1" stop-color="var(--leaf-green-deep)"/>
    </radialGradient>
    <radialGradient id="ginger-tone" cx="45%" cy="50%" r="55%">
      <stop offset="0" stop-color="#dcbf8e"/>
      <stop offset=".7" stop-color="var(--ginger-tan)"/>
      <stop offset="1" stop-color="#b98f55" stop-opacity="0"/>
    </radialGradient>
    <clipPath id="pouch-shape"><rect width="600" height="860" rx="6"/></clipPath>
  </defs>

  <g clip-path="url(#pouch-shape)">
    <rect class="pouch-body" width="600" height="860" fill="var(--pouch-white)"/>

    <rect class="swirl-field" y="0" width="600" height="620" fill="url(#field-green)"
          role="img" aria-label="Green background with a swirling decorative pattern and sunburst rays"/>

    <path class="top-crimp" d="M0 0H600V112L305 78L0 112Z" fill="url(#crimp-top)"/>
    <path class="green-ribbon" d="M0 112L305 78L600 112V130L305 96L0 130Z" fill="var(--leaf-green-light)"/>

    <path class="yellow-arc" d="M0 575Q300 470 600 575V860H0Z" fill="var(--sun-yellow)"/>
    <path class="white-panel" d="M0 602Q300 505 600 602V860H0Z" fill="var(--pouch-white)"/>

    <rect class="bottom-crimp" y="812" width="600" height="48" fill="url(#crimp-bottom)"/>
  </g>

  <g class="brand-pennant">
    <path d="M195 0H415V110L305 168L195 110Z" fill="var(--sky-blue)"/>
    <path d="M201 0H409V106L305 160L201 106Z" fill="var(--navy)"/>
    <path d="M206 0H404V102L305 153L206 102Z" fill="url(#pennant-lines)"/>
    <text class="brand-mark" x="305" y="132" text-anchor="middle" font-size="40">Tolvo</text>
  </g>

  <text class="product-name" x="300" y="355" text-anchor="middle" font-size="96">Gintolvo</text>

  <g class="flavour-banner">
    <path d="M118 420H494L484 472H108Z" fill="var(--navy)"/>
    <path d="M124 425H488L479 467H115Z" fill="none" stroke="#fff" stroke-width="1" stroke-dasharray="3 3" opacity=".7"/>
    <text class="flavour-banner-text" x="300" y="458" text-anchor="middle" font-size="31">GINGER CHEWY CANDY</text>
  </g>

  <ellipse class="ginger-photo" cx="305" cy="622" rx="195" ry="112" fill="url(#ginger-tone)"
           role="img" aria-label="Photograph of a fresh ginger root with golden sliced rounds"/>

  <text class="tagline-shadow" x="301" y="759" text-anchor="middle" font-size="19">...a good relief for sore throat and nausea.</text>
  <text class="tagline" x="300" y="757" text-anchor="middle" font-size="19">...a good relief for sore throat and nausea.</text>
  <text class="net-weight" x="305" y="800" text-anchor="middle" font-size="22">NET WT 4 OZ</text>
</svg>
</body>
</html>
```